Design business cards for Ironvale Barbers (Opening March so won't need finalised till January2018

Ironvale Barbers is the new age barbers and skincare for all men. Creating tailor made haircuts & customised skincare solutions for the perfect healthy manly look. The Barbers will have a industrial, rustic, worldly feel about it. Rustic red brick wall with old wine barrels as the work stations with the old fashion barber chairs. Concrete floor and a bit corrugated iron around.
Target Market(s)
Professional males who like a great haircut, wet shave and may consider a facial if in the right environment. Total pampering experience in a boys environment.
Industry/Entity Type
Barber
Contact Information for Business Card
Front- Logo - address is 42 Kowhai Rd Taupo
Ph - (07) 548 9163
www.ironvalebarbers.com
email - hello@ironvale.co.nz
Back of card
Mens Haircare - Wet Shaving - Facials - Skin Prescriptions
We are doing a loyalty program - 6 squares numbered then 7th free
Colors
Designer to choose colors to be used in the design.
Requirements
Must have
- Clean simple easy to read.
Nice to have
- Our current colours are white font on black background but thinking we need to introduce another colour. Maybe white logo on a copper, bronze or rusty background. Or even a rustic red brick wall with white writing. Want it clean simple to read. Maybe a burgundy?
Should not have
- no images like heads, scissors, razors please

```html
<!DOCTYPE html>
<html lang="en">
<head>
<meta charset="utf-8">
<title>Ironvale Barbers – Business Cards</title>
<link rel="stylesheet" href="https://fonts.googleapis.com/css2?family=Tinos:wght@400;700&display=swap">
<style>
  :root {
    --page: #e6e3df;
    --wood-light: #c9662c;
    --wood-mid: #b4531f;
    --wood-dark: #8b3713;
    --hoop: #8f7a64;
    --hoop-edge: #5e4a38;
    --ink: #47200b;
    --ink-soft: #5a2a10;
    --box: #6b2e10;
    --box-text: #d98a52;
  }
  * { box-sizing: border-box; margin: 0; padding: 0; }
  html, body {
    width: 1200px; height: 1200px; overflow: hidden;
    background: var(--page);
    font-family: "Tinos", "Times New Roman", serif;
    color: var(--ink);
  }
  .card {
    position: absolute;
    left: 244px;
    width: 748px;
    height: 428px;
    border-radius: 22px;
    overflow: hidden;
    box-shadow: 0 10px 24px rgba(0,0,0,0.25);
  }
  .card--front { top: 102px; }
  .card--back { top: 646px; }
  .card__surface { position: absolute; inset: 0; width: 100%; height: 100%; }

  .brand {
    position: absolute; left: 0; right: 0; top: 92px;
    text-align: center; font-weight: 700; color: var(--ink);
    line-height: 1;
  }
  .brand__name { display: block; font-size: 60px; letter-spacing: 1px; }
  .brand__sub { display: block; font-size: 22px; letter-spacing: 7px; margin-top: 8px; }

  .person {
    position: absolute; right: 398px; top: 238px; text-align: right;
    font-weight: 700;
  }
  .person__name { font-size: 26px; letter-spacing: 0.5px; }
  .person__role { font-size: 18px; margin-top: 8px; color: var(--ink-soft); }

  .divider {
    position: absolute; left: 377px; top: 218px; width: 2px; height: 121px;
    background: var(--ink);
  }

  .contacts { position: absolute; left: 398px; top: 216px; list-style: none; }
  .contacts li {
    display: flex; align-items: center; height: 33px;
    font-size: 19px; font-weight: 700; color: var(--ink);
  }
  .contacts svg { width: 14px; height: 14px; margin-right: 12px; fill: var(--ink); flex: none; }

  .services {
    position: absolute; left: 36px; top: 183px;
    font-size: 24px; font-weight: 700; color: var(--ink); white-space: nowrap;
  }
  .loyalty {
    position: absolute; left: 36px; top: 229px;
    display: flex; align-items: center;
    font-size: 24px; font-weight: 700; color: var(--ink); white-space: nowrap;
  }
  .loyalty__boxes { display: flex; gap: 5px; margin-left: 10px; }
  .loyalty__box {
    width: 24px; height: 24px; background: var(--box);
    color: var(--box-text); font-size: 19px; line-height: 24px; text-align: center;
  }
  .loyalty__box--free { width: 74px; margin-left: 6px; font-size: 17px; }
</style>
</head>
<body>

<section class="card card--front">
  <svg class="card__surface" viewBox="0 0 748 428" preserveAspectRatio="none">
    <defs>
      <linearGradient id="woodFront" x1="0" y1="0" x2="1" y2="0">
        <stop offset="0" stop-color="var(--wood-dark)"/>
        <stop offset="0.3" stop-color="var(--wood-mid)"/>
        <stop offset="0.55" stop-color="var(--wood-light)"/>
        <stop offset="0.8" stop-color="var(--wood-mid)"/>
        <stop offset="1" stop-color="var(--wood-dark)"/>
      </linearGradient>
    </defs>
    <rect width="748" height="428" fill="url(#woodFront)" role="img" aria-label="Oak wine barrel wood grain"/>
    <path class="hoop" d="M0 42 Q374 14 748 42 L748 74 Q374 46 0 74 Z" fill="var(--hoop)" stroke="var(--hoop-edge)" stroke-width="2"/>
    <path class="hoop" d="M0 356 Q374 384 748 356 L748 392 Q374 420 0 392 Z" fill="var(--hoop)" stroke="var(--hoop-edge)" stroke-width="2"/>
  </svg>

  <div class="brand">
    <span class="brand__name">IRONVALE</span>
    <span class="brand__sub">BARBERS</span>
  </div>

  <div class="person">
    <div class="person__name">YOURNAME</div>
    <div class="person__role">Designation</div>
  </div>

  <div class="divider"></div>

  <ul class="contacts">
    <li>
      <svg viewBox="0 0 24 24"><path d="M6.6 10.8a15 15 0 0 0 6.6 6.6l2.2-2.2c.3-.3.7-.4 1-.2 1.1.4 2.3.6 3.6.6.6 0 1 .4 1 1V20c0 .6-.4 1-1 1C10.6 21 3 13.4 3 4c0-.6.4-1 1-1h3.5c.6 0 1 .4 1 1 0 1.3.2 2.5.6 3.6.1.3 0 .7-.2 1z"/></svg>
      (07) 548 9163
    </li>
    <li>
      <svg viewBox="0 0 24 24"><path d="M2 5h20v14H2z M3 6l9 7 9-7" fill="none" stroke="currentColor" stroke-width="0"/><path d="M2 5h20v2l-10 7L2 7z M2 9l10 7 10-7v10H2z"/></svg>
      hello@ironvale.co.nz
    </li>
    <li>
      <svg viewBox="0 0 24 24"><path d="M12 2a7 7 0 0 0-7 7c0 5 7 13 7 13s7-8 7-13a7 7 0 0 0-7-7zm0 9.5A2.5 2.5 0 1 1 12 6.5a2.5 2.5 0 0 1 0 5z"/></svg>
      42 Kowhai Rd Taupo
    </li>
    <li>
      <svg viewBox="0 0 24 24"><path d="M10 14l4-4M8.5 11.5l-3 3a3 3 0 0 0 4 4l3-3M15.5 12.5l3-3a3 3 0 0 0-4-4l-3 3" fill="none" stroke="var(--ink)" stroke-width="2.2" stroke-linecap="round"/></svg>
      www.ironvalebarbers.com
    </li>
  </ul>
</section>

<section class="card card--back">
  <svg class="card__surface" viewBox="0 0 748 428" preserveAspectRatio="none">
    <defs>
      <linearGradient id="woodBack" x1="0" y1="0" x2="1" y2="0">
        <stop offset="0" stop-color="var(--wood-dark)"/>
        <stop offset="0.3" stop-color="var(--wood-mid)"/>
        <stop offset="0.55" stop-color="var(--wood-light)"/>
        <stop offset="0.8" stop-color="var(--wood-mid)"/>
        <stop offset="1" stop-color="var(--wood-dark)"/>
      </linearGradient>
    </defs>
    <rect width="748" height="428" fill="url(#woodBack)" role="img" aria-label="Oak wine barrel wood grain"/>
    <path class="hoop" d="M0 54 Q374 14 748 54 L748 86 Q374 46 0 86 Z" fill="var(--hoop)" stroke="var(--hoop-edge)" stroke-width="2"/>
    <path class="hoop" d="M0 356 Q374 382 748 356 L748 390 Q374 416 0 390 Z" fill="var(--hoop)" stroke="var(--hoop-edge)" stroke-width="2"/>
  </svg>

  <p class="services">Mens Haircare - Wet Shaving - Facials - Skin Prescriptions</p>
  <div class="loyalty">
    <span>We are doing a loyalty program -</span>
    <div class="loyalty__boxes">
      <span class="loyalty__box">1</span>
      <span class="loyalty__box">2</span>
      <span class="loyalty__box">3</span>
      <span class="loyalty__box">4</span>
      <span class="loyalty__box">5</span>
      <span class="loyalty__box">6</span>
      <span class="loyalty__box loyalty__box--free">FREE</span>
    </div>
  </div>
</section>

</body>
</html>
```